Roll-Up Banner für Glückswebsite
Das war eine großartige Zusammenarbeit und unserem sehr knappen Zeitplan extrem entgegenkommend. Das design ist gleichzeitig seriös und trotzdem jung und dynamisch! Perfekt!
Zielgruppe
Die Website, www.freudenpfad.de ermöglicht es jedem Interessierten kostenlos mehr über das eigene Lebensglück, persönliche Stärken, und die eigene Lebenszufriedenheit herauszufinden. Interessierte können online Fragebögen ausfüllen, und erhalten neben einer detaillierten Rückmeldung über die eigenen Möglichkeiten und Stärken, Hinweise dazu, wie Sie an Ihrem eigenen Potenzial arbeiten können. Es handelt sich um ein Kooperationsprojekt der Nordischen Vereinigung für Heitere Seelenkunde der Uni Wendelstein, der HK-Lindau, der Health Academy Marbach und der Uni Falkenried. Zielgruppe für das Banner sind Menschen, die selbst mit Klienten im Kontext der Positiven Psychologie arbeiten oder Menschen, die sich Ihrem eigenen Lebensglück zuwenden wollen.
Aufgabenstellung
Es handelt sich um ein Roll-up Banner in den Maßen 1m Breite und 2 Meter Höhe.
Das Banner sollte so angelegt sein, dass es interessierten Besuchern auf Kongressen vermittelt, was es mit der Seite Freudenpfad.de auf sich hat. Also wissenschaftlich evaluierte kostenfreie online-Fragebögen, die Menschen dabei helfen Ihre eigenen Stärken und Potenziale zu entdecken und dem eigenen Glück näher zu kommen.
Es sollte außerdem das Logo der NVHS darauf zu sehen sein, sowie kleiner die Logos der Forschungskooperationspartner, HK-Lindau, Uni Wendelstein, Uni Falkenried, Health Academy Marbach.
Die Farben sollten zum Logo der NVHS passen.

```html
<!DOCTYPE html>
<html lang="de">
<head>
<meta charset="utf-8">
<title>Freudenpfad.de – Roll-up Banner</title>
<link rel="stylesheet" href="https://fonts.googleapis.com/css2?family=PT+Sans:wght@400;700&family=PT+Sans+Narrow:wght@700&display=swap">
<style>
  :root {
    --navy: #1e3a7b;
    --teal: #1f9a9c;
    --teal-top-a: #6aa596;
    --teal-top-b: #4e9c9f;
    --green: #9cc040;
    --green-mid: #86b262;
    --white: #ffffff;
    --ink: #1b1b1b;
    --photo-light: #e4dcc4;
    --photo-mid: #a89a86;
    --photo-dark: #5a5053;
  }
  * { margin: 0; padding: 0; box-sizing: border-box; }
  html, body { width: 1200px; height: 2400px; overflow: hidden; background: var(--white); }
  body { font-family: "PT Sans", sans-serif; }

  .banner { position: relative; width: 1200px; height: 2400px; overflow: hidden; }

  .brand-panel {
    position: absolute; left: 0; top: 0; width: 416px; height: 450px;
    background: linear-gradient(to bottom, var(--white) 88%, #e6e6e6 100%);
  }
  .brand-mark {
    position: absolute; left: 70px; top: 110px; width: 150px; height: 150px;
    border-radius: 50%; background: var(--teal);
  }
  .brand-name {
    position: absolute; left: 142px; top: 274px;
    font: 700 50px/1 "PT Sans", sans-serif; color: var(--navy); letter-spacing: 2px;
  }
  .brand-full {
    position: absolute; left: 144px; top: 337px; width: 270px;
    font: 400 20px/26px "PT Sans", sans-serif; color: var(--navy);
  }

  .headline-panel {
    position: absolute; left: 416px; top: 0; width: 784px; height: 450px;
    background: linear-gradient(100deg, var(--teal-top-a) 0%, var(--teal-top-b) 60%, #54a0a0 100%);
  }
  .headline-panel::after {
    content: ""; position: absolute; left: 0; right: 0; bottom: 0; height: 36px;
    background: linear-gradient(to bottom, rgba(0,0,0,0), rgba(0,0,0,0.22));
  }
  .site-title {
    position: absolute; left: 29px; top: 110px;
    font: 700 108px/1 "PT Sans Narrow", sans-serif; color: var(--white); letter-spacing: -1px;
  }
  .site-claim {
    position: absolute; left: 29px; top: 282px; width: 740px;
    font: 400 42px/60px "PT Sans", sans-serif; color: var(--white);
  }

  .hero-photo {
    position: absolute; left: 0; top: 450px; width: 1200px; height: 1108px;
    background: linear-gradient(to bottom, var(--photo-light) 0%, var(--photo-mid) 50%, var(--photo-dark) 100%);
  }

  .partners-panel {
    position: absolute; left: 0; top: 1558px; width: 416px; height: 842px;
    background: linear-gradient(to bottom, #e8e8e8 0%, var(--white) 5%);
  }
  .partners-label {
    position: absolute; left: 66px; top: 1614px;
    font: 700 24px/1 "PT Sans", sans-serif; color: var(--ink);
  }
  .partner {
    position: absolute; left: 68px; display: flex; align-items: center; gap: 14px;
    font: 400 24px/1.15 "PT Sans", sans-serif; color: var(--navy); white-space: nowrap;
  }
  .partner-dot { width: 40px; height: 40px; border-radius: 50%; background: var(--navy); flex: none; }
  .partner-1 { top: 1740px; }
  .partner-2 { top: 1890px; }
  .partner-3 { top: 2016px; }
  .partner-4 { top: 2152px; }

  .message-panel {
    position: absolute; left: 416px; top: 1558px; width: 784px; height: 842px;
    background: linear-gradient(200deg, var(--teal) 0%, var(--green-mid) 45%, var(--green) 100%);
  }
  .message-panel::before {
    content: ""; position: absolute; left: 0; right: 0; top: 0; height: 24px;
    background: linear-gradient(to bottom, rgba(0,0,0,0.15), rgba(0,0,0,0));
  }
  .message {
    position: absolute; left: 39px; top: 50px; width: 720px;
    font: 400 41px/59px "PT Sans", sans-serif; color: var(--white);
  }
</style>
</head>
<body>
<main class="banner">
  <section class="brand-panel">
    <div class="brand-mark"></div>
    <div class="brand-name">NVHS</div>
    <div class="brand-full">Nordische Vereinigung für<br><strong>Heitere Seelenkunde</strong></div>
  </section>

  <header class="headline-panel">
    <h1 class="site-title">Freudenpfad.de</h1>
    <p class="site-claim">Wissenschaftlich evaluierte kostenfreie<br>online-Fragebögen.</p>
  </header>

  <div class="hero-photo" role="img" aria-label="Foto: lachendes Kind mit Fliegerhaube und selbstgebastelten Pappflügeln auf einer Landstraße im warmen Abendlicht"></div>

  <aside class="partners-panel"></aside>
  <div class="partners-label">Forschungskooperation</div>
  <div class="partner partner-1"><span class="partner-dot"></span>Uni Wendelstein</div>
  <div class="partner partner-2"><span class="partner-dot"></span>HK-Lindau</div>
  <div class="partner partner-3"><span class="partner-dot"></span>Health Academy Marbach</div>
  <div class="partner partner-4"><span class="partner-dot"></span>Uni Falkenried</div>

  <section class="message-panel">
    <p class="message">Entdecken Sie ihre Stärken und Ihr<br>Potenzial um Ihrem eigenen Glück<br>näher zu kommen.</p>
  </section>
</main>
</body>
</html>
```